Health care technology software systems

We have a solid logo. We have company colors that will need to be used as well. We just need a great business card design. We sell to health plans but want to be modern

Target Market(s)

Health technology sector selling into Health Plans

Industry/Entity Type

Health Care Technology

Contact Information for Business Card

Name, title, address, phone number, email

Requirements
Must have
• Use of Parvexa corporate colors - Uploaded w/ our logos

```html
<!DOCTYPE html>
<html lang="en">
<head>
<meta charset="utf-8">
<title>Parvexa Business Card</title>
<link href="https://fonts.googleapis.com/css2?family=Poppins:wght@300;400;600&display=swap" rel="stylesheet">
<style>
  :root {
    --page: #1c1c1c;
    --card: #353635;
    --white: #ffffff;
    --muted: #e4e4e4;
    --sky: #16a3dd;
    --indigo: #3d56a6;
    --lime: #8cc63f;
  }
  * { margin: 0; padding: 0; box-sizing: border-box; }
  html, body { width: 1200px; height: 900px; overflow: hidden; }
  body {
    background: var(--page);
    font-family: "Poppins", sans-serif;
    color: var(--white);
    display: flex;
    flex-direction: column;
    align-items: center;
    justify-content: center;
    gap: 40px;
  }
  .card {
    position: relative;
    width: 700px;
    height: 400px;
    background: var(--card);
    box-shadow: 0 12px 30px rgba(0,0,0,.5);
    overflow: hidden;
  }
  .brand {
    display: flex;
    align-items: center;
    gap: 18px;
    font-weight: 300;
    color: var(--white);
    letter-spacing: 2px;
  }
  .brand-dot {
    width: 38px; height: 38px;
    border-radius: 50%;
    background: var(--sky);
  }
  .brand-name { font-size: 58px; line-height: 1; }

  /* front */
  .card-front .brand { position: absolute; top: 44px; left: 200px; }
  .contact { position: absolute; top: 170px; left: 48px; }
  .person-name { font-size: 26px; font-weight: 600; letter-spacing: .5px; }
  .person-title { font-size: 16px; color: var(--lime); margin-top: 2px; }
  .divider {
    position: absolute; top: 232px; left: 210px; right: 48px;
    height: 1px; background: var(--lime);
  }
  .contact-list { list-style: none; margin-top: 22px; }
  .contact-list li {
    display: flex; align-items: center; gap: 12px;
    font-size: 15px; color: var(--muted); margin-bottom: 6px;
  }
  .contact-list svg { width: 15px; height: 15px; flex: none; }
  .address {
    position: absolute; right: 48px; bottom: 62px;
    display: flex; gap: 10px;
    font-size: 15px; color: var(--muted); line-height: 1.45;
  }
  .address svg { width: 15px; height: 18px; margin-top: 3px; flex: none; }
  .color-band {
    position: absolute; left: 0; right: 0; bottom: 0; height: 16px;
    display: flex;
  }
  .color-band span { flex: 1; }
  .band-sky { background: var(--sky); }
  .band-indigo { background: var(--indigo); }
  .band-lime { background: var(--lime); }

  /* back */
  .card-back {
    display: flex; flex-direction: column;
    align-items: center; justify-content: center; gap: 40px;
  }
  .card-back .brand-name { font-size: 72px; }
  .web { font-size: 18px; color: var(--muted); letter-spacing: 1px; }
</style>
</head>
<body>

  <section class="card card-front" aria-label="Business card front">
    <div class="brand">
      <span class="brand-dot"></span>
      <span class="brand-name">parvexa</span>
    </div>

    <div class="contact">
      <h1 class="person-name">Daniel Harper</h1>
      <p class="person-title">CEO/Founder</p>
      <ul class="contact-list">
        <li>
          <svg viewBox="0 0 24 24" fill="var(--sky)"><path d="M6.6 10.8a15 15 0 0 0 6.6 6.6l2.2-2.2a1 1 0 0 1 1-.25 11.4 11.4 0 0 0 3.6.57 1 1 0 0 1 1 1V20a1 1 0 0 1-1 1A17 17 0 0 1 3 4a1 1 0 0 1 1-1h3.5a1 1 0 0 1 1 1c0 1.25.2 2.45.57 3.57a1 1 0 0 1-.25 1z"/></svg>
          555-203-4817
        </li>
        <li>
          <svg viewBox="0 0 24 24" fill="none" stroke="var(--sky)" stroke-width="2.2"><rect x="3" y="5" width="18" height="14" rx="1"/><path d="M3 6l9 7 9-7"/></svg>
          daniel@parvexamail.com
        </li>
        <li>
          <svg viewBox="0 0 24 24" fill="none" stroke="var(--sky)" stroke-width="2"><circle cx="12" cy="12" r="9"/><path d="M3 12h18M12 3c3 3 3 15 0 18M12 3c-3 3-3 15 0 18"/></svg>
          www.parvexahealth.com
        </li>
      </ul>
    </div>

    <div class="divider"></div>

    <div class="address">
      <svg viewBox="0 0 20 24" fill="none" stroke="var(--sky)" stroke-width="2.6"><path d="M10 22s7-7.5 7-12.5A7 7 0 0 0 3 9.5C3 14.5 10 22 10 22z"/><circle cx="10" cy="9.5" r="2.4"/></svg>
      <p>410 Harlow Street<br>Suite 200, Millbrook<br>MI 49210</p>
    </div>

    <div class="color-band">
      <span class="band-sky"></span>
      <span class="band-indigo"></span>
      <span class="band-lime"></span>
    </div>
  </section>

  <section class="card card-back" aria-label="Business card back">
    <div class="brand">
      <span class="brand-dot"></span>
      <span class="brand-name">parvexa</span>
    </div>
    <p class="web">www.parvexa.com</p>
  </section>

</body>
</html>
```